Create Lanternfield HR Business Cards.

Create Business Cards for Lanternfield HR. 2 sided and Would like the back to have the logo.

Info for Business Card:
Address: 4827 Millbrook Ave Suite 230 Cleveland, Ohio 44987
Office Number: 216-555-0143
Mobile: 216-555-0192

Website: www.lanternfieldhr.example

Target Market(s)

Small to medium size businesses

Industry/Entity Type

Human Resources

Contact Information for Business Card

Company logo and information

Font styles to use
Serif
Sans Serif

Requirements
Must have
• Info for Business Card: Address: 4827 Millbrook Ave Suite 230 Cleveland, Ohio 44987 Office Number: 216-555-0143 Mobile: 216-555-0192 Website: www.lanternfieldhr.example

```html
<!DOCTYPE html>
<html lang="en">
<head>
<meta charset="utf-8">
<title>Lanternfield HR Business Cards</title>
<link href="https://fonts.googleapis.com/css2?family=Montserrat:wght@600;700&display=swap" rel="stylesheet">
<style>
  :root {
    --page-bg: #e4e4e6;
    --front-top: #3a2b62;
    --front-mid: #5e3560;
    --front-bottom: #a0574c;
    --back-top: #ffffff;
    --back-bottom: #dcdcde;
    --ink: #1d1d1f;
    --brand-navy: #2c2c6e;
    --brand-orange: #f28a2e;
    --logo-light: #ececec;
  }
  * { box-sizing: border-box; margin: 0; padding: 0; }
  html, body {
    width: 1200px; height: 1200px; overflow: hidden;
    background: var(--page-bg);
    font-family: "Montserrat", Arial, sans-serif;
  }
  .sheet {
    width: 1200px; height: 1200px;
    display: flex; flex-direction: column; align-items: center; justify-content: center;
    gap: 48px;
  }
  .card {
    width: 900px; height: 514px;
    border-radius: 4px;
    box-shadow: 0 10px 30px rgba(0,0,0,0.18);
    position: relative; overflow: hidden;
  }
  .card-front {
    background: linear-gradient(30deg, var(--front-bottom) 0%, var(--front-mid) 50%, var(--front-top) 100%);
    display: flex; align-items: center; justify-content: center;
  }
  .brand {
    display: flex; align-items: center; gap: 18px;
    font-weight: 700; font-size: 52px; letter-spacing: 0.5px;
  }
  .brand-mark {
    width: 40px; height: 40px; border-radius: 50%; flex: none;
  }
  .card-front .brand { color: var(--logo-light); }
  .card-front .brand-mark { background: var(--logo-light); }

  .card-back {
    background: linear-gradient(180deg, var(--back-top) 0%, #f4f4f5 45%, var(--back-bottom) 100%);
  }
  .card-back .brand {
    position: absolute; left: 60px; top: 300px;
    color: var(--brand-navy); font-size: 36px; gap: 14px;
  }
  .card-back .brand-mark { width: 30px; height: 30px; background: var(--brand-orange); }

  .contact {
    position: absolute; left: 440px; top: 70px;
    color: var(--ink); font-weight: 700;
  }
  .contact-row { display: flex; align-items: center; gap: 14px; margin-bottom: 26px; }
  .contact-icon { width: 26px; height: 30px; flex: none; fill: var(--ink); }
  .contact-lines {
    border-left: 2px solid var(--ink); padding-left: 12px;
    font-size: 27px; line-height: 1.22;
  }
  .contact-web { font-size: 25px; font-weight: 600; padding-left: 40px; letter-spacing: 0.5px; }
</style>
</head>
<body>
  <main class="sheet">
    <section class="card card-front" aria-label="Card front">
      <div class="brand"><span class="brand-mark"></span><span class="brand-name">Lanternfield HR</span></div>
    </section>

    <section class="card card-back" aria-label="Card back">
      <div class="brand"><span class="brand-mark"></span><span class="brand-name">Lanternfield HR</span></div>

      <div class="contact">
        <div class="contact-row">
          <svg class="contact-icon" viewBox="0 0 24 30" aria-hidden="true">
            <path d="M12 0C5.4 0 0 5.2 0 11.6 0 20 12 30 12 30s12-10 12-18.4C24 5.2 18.6 0 12 0zm0 16.5a5 5 0 1 1 0-10 5 5 0 0 1 0 10z"/>
          </svg>
          <address class="contact-lines" style="font-style:normal">
            4827 Millbrook Ave<br>Suite 230 Cleveland<br>Ohio 44987
          </address>
        </div>
        <div class="contact-row">
          <svg class="contact-icon" viewBox="0 0 24 24" aria-hidden="true">
            <path d="M6.6 10.8a15.1 15.1 0 0 0 6.6 6.6l2.2-2.2c.3-.3.7-.4 1-.2 1.1.4 2.3.6 3.6.6.6 0 1 .4 1 1V20c0 .6-.4 1-1 1A17 17 0 0 1 3 4c0-.6.4-1 1-1h3.5c.6 0 1 .4 1 1 0 1.3.2 2.5.6 3.6.1.3 0 .7-.2 1z"/>
          </svg>
          <div class="contact-lines">
            216-555-0143<br>216-555-0192
          </div>
        </div>
        <div class="contact-web">www.lanternfieldhr.example</div>
      </div>
    </section>
  </main>
</body>
</html>
```